Laundromat Grand Opening.

Laundromat /Grand opening. One side English, one side Spanish. Include the Address, Name, Raffle/Prizes and Grand opening date.
Elmridge Wash Laundromat, 415 W. Harlan Ave. 2/7/2016. (555) 314-2297.

Coin

000000

• Eye catching. Laundry theme.

```html
<!DOCTYPE html>
<html lang="en">
<head>
<meta charset="utf-8">
<title>Elmridge Wash Laundry – Grand Opening Flyers</title>
<link href="https://fonts.googleapis.com/css2?family=Arimo:wght@400;700&family=Great+Vibes&family=PT+Sans+Narrow&display=swap" rel="stylesheet">
<style>
  :root {
    --page-bg: #e6e4e1;
    --flyer-black: #000000;
    --text-white: #ffffff;
    --text-silver: #d9d9d9;
    --text-grey: #bdbdbd;
    --rule-grey: #9a9a9a;
    --photo-light: #c4c8cb;
    --photo-mid: #a9aeb2;
    --photo-dark: #8e9397;
    --tag-fill: #ececec;
    --tag-edge: #8f8f8f;
    --tag-text: #2a2a2a;
  }
  html, body {
    margin: 0;
    padding: 0;
    width: 1200px;
    height: 903px;
    overflow: hidden;
    background: var(--page-bg);
  }
  .sheet {
    position: relative;
    width: 1200px;
    height: 903px;
  }
  .flyer {
    position: absolute;
    top: 84px;
    width: 493px;
    height: 723px;
    background: var(--flyer-black);
    font-family: "Arimo", Arial, sans-serif;
    color: var(--text-white);
    box-shadow: 4px 6px 12px rgba(0,0,0,0.25);
  }
  .flyer--english { left: 68px; }
  .flyer--spanish { left: 636px; }

  .flyer__business {
    position: absolute;
    top: 24px;
    left: 0;
    width: 100%;
    text-align: center;
    font-size: 22px;
    letter-spacing: 0.5px;
    margin: 0;
    font-weight: 400;
  }
  .flyer--spanish .flyer__business { font-size: 20px; top: 26px; }
  .flyer__headline {
    position: absolute;
    top: 60px;
    left: 0;
    width: 100%;
    text-align: center;
    font-family: "Great Vibes", cursive;
    font-size: 70px;
    font-weight: 400;
    letter-spacing: 2px;
    line-height: 1;
    margin: 0;
    color: var(--text-silver);
    white-space: nowrap;
  }
  .flyer--spanish .flyer__headline { font-size: 64px; letter-spacing: 1px; top: 63px; }

  .flyer__photo {
    position: absolute;
    top: 143px;
    left: 0;
    width: 493px;
    height: 382px;
    background: linear-gradient(180deg, var(--photo-light) 0%, var(--photo-mid) 60%, var(--photo-dark) 100%);
  }

  .raffle-tag {
    position: absolute;
    top: 413px;
    left: 314px;
    width: 155px;
    height: 84px;
    background: var(--tag-fill);
    border: 2px dashed var(--tag-edge);
    border-radius: 8px;
    box-sizing: border-box;
    font-family: "PT Sans Narrow", "Arial Narrow", sans-serif;
    text-align: center;
    color: var(--tag-text);
  }
  .raffle-tag__icons {
    display: block;
    margin: 6px auto 0;
  }
  .raffle-tag__title {
    display: block;
    font-size: 25px;
    line-height: 1;
    margin-top: 4px;
  }
  .raffle-tag__name {
    display: block;
    font-family: "Arimo", Arial, sans-serif;
    font-size: 9.5px;
    color: #555;
    margin-top: 6px;
  }

  .flyer__date {
    position: absolute;
    top: 561px;
    left: 0;
    width: 100%;
    text-align: center;
    font-size: 30px;
    font-weight: 700;
    margin: 0;
    letter-spacing: 0.3px;
  }
  .flyer__rule {
    position: absolute;
    top: 601px;
    left: 135px;
    width: 255px;
    border-top: 2px dotted var(--rule-grey);
  }
  .flyer--spanish .flyer__rule { left: 118px; width: 255px; }
  .flyer__hours {
    position: absolute;
    top: 612px;
    left: 0;
    width: 100%;
    text-align: center;
    font-size: 21px;
    margin: 0;
  }
  .flyer__contact {
    position: absolute;
    top: 676px;
    left: 0;
    width: 100%;
    text-align: center;
    font-size: 13.5px;
    color: var(--text-grey);
    margin: 0;
  }
</style>
</head>
<body>
<main class="sheet">

  <article class="flyer flyer--english" lang="en">
    <h2 class="flyer__business">ELMRIDGE WASH LAUNDRY</h2>
    <h1 class="flyer__headline">Grand Opening</h1>
    <div class="flyer__photo" role="img" aria-label="Photo area: row of stainless steel front-loading washing machines in a laundromat"></div>
    <div class="raffle-tag">
      <svg class="raffle-tag__icons" width="60" height="10" viewBox="0 0 60 10" aria-hidden="true">
        <g fill="none" stroke="#555" stroke-width="1">
          <rect x="2" y="1" width="9" height="8"/>
          <circle cx="23" cy="5" r="4"/>
          <rect x="34" y="1" width="9" height="8"/>
          <path d="M49 9 L54 1 L59 9 Z"/>
        </g>
      </svg>
      <span class="raffle-tag__title">Raffle/Prizes</span>
      <span class="raffle-tag__name">Elmridge Wash Laundromat</span>
    </div>
    <p class="flyer__date">FEB 7TH. 2016</p>
    <div class="flyer__rule"></div>
    <p class="flyer__hours">Time 7:00 a.m till 10:00p.m</p>
    <p class="flyer__contact">415 W. Harlan Ave. Elmridge, CA 91700 &nbsp;| &nbsp;(555) 314-2297</p>
  </article>

  <article class="flyer flyer--spanish" lang="es">
    <h2 class="flyer__business">ELMRIDGE LAVANDERÍA</h2>
    <h1 class="flyer__headline">Gran Inauguración</h1>
    <div class="flyer__photo" role="img" aria-label="Área de foto: fila de lavadoras de acero inoxidable de carga frontal en una lavandería"></div>
    <div class="raffle-tag">
      <svg class="raffle-tag__icons" width="60" height="10" viewBox="0 0 60 10" aria-hidden="true">
        <g fill="none" stroke="#555" stroke-width="1">
          <rect x="2" y="1" width="9" height="8"/>
          <circle cx="23" cy="5" r="4"/>
          <rect x="34" y="1" width="9" height="8"/>
          <path d="M49 9 L54 1 L59 9 Z"/>
        </g>
      </svg>
      <span class="raffle-tag__title">Rifa/Premios</span>
      <span class="raffle-tag__name">Elmridge Wash Laundromat</span>
    </div>
    <p class="flyer__date">FEBRERO 7º. 2016</p>
    <div class="flyer__rule"></div>
    <p class="flyer__hours">7:00 am hasta las 10:00 pm</p>
    <p class="flyer__contact">415 W. Harlan Ave. Elmridge, CA 91700 &nbsp;| &nbsp;(555) 314-2297</p>
  </article>

</main>
</body>
</html>
```